Leaflets
We supply stone and solid surfaces to the trade and project manage its installation
Project: Leaflets
Leaflets - Construction
Creative Brief
Construction
Architects, Interior designers, property developers, kitchen and bathroom designers, shopfitters Our offer is mainly business to business. Our branding and images are corporate and our content (wording) is more casual (which is what makes us different from the competition)
A leaflet with our branding, logos and fonts to be used as an introduction to our clients mainly targeted trough site visits and by posting samples. Images and branding available on request.

```html
<!DOCTYPE html>
<html lang="en">
<head>
<meta charset="utf-8">
<title>Trelvax – Stone and Solid Surfaces Leaflet</title>
<link href="https://fonts.googleapis.com/css2?family=Arimo:wght@400;700&display=swap" rel="stylesheet">
<style>
  :root {
    --green: #8dc63f;
    --purple: #5b2c8f;
    --tile-gap: #d4d4d4;
    --white: #ffffff;
    --text-dark: #2b2b2b;
  }
  html, body { margin: 0; padding: 0; overflow: hidden; background: #eeeeee; }
  .leaflet {
    position: relative; width: 1200px; height: 845px; overflow: hidden;
    background: var(--tile-gap); font-family: "Arimo", Arial, sans-serif; color: var(--text-dark);
  }
  .block { position: absolute; box-sizing: border-box; }
  .tile-white { background: var(--white); }
  .tile-green { background: var(--green); }
  .tile-purple { background: var(--purple); }
  .photo::after {
    content: ""; position: absolute; inset: 0;
    background:
      repeating-linear-gradient(90deg, transparent 0 64px, rgba(255,255,255,.55) 64px 70px),
      repeating-linear-gradient(0deg, transparent 0 64px, rgba(255,255,255,.55) 64px 70px);
  }
  .photo-kitchen-main { left: 0; top: 269px; width: 662px; height: 380px;
    background: linear-gradient(170deg, #8a8078 0%, #b9ab9c 40%, #d9cbb9 65%, #8d7f71 100%); }
  .photo-kitchen-bright { left: 665px; top: 0; width: 535px; height: 285px;
    background: linear-gradient(160deg, #e7e9ea 0%, #cfd6d8 45%, #b7c1bf 75%, #9aa6a3 100%); }
  .photo-island { left: 800px; top: 384px; width: 400px; height: 266px;
    background: linear-gradient(175deg, #c6cfcc 0%, #9fa9a2 35%, #6e5d4c 70%, #a69a8a 100%); }

  .brand { left: 0; top: 0; width: 340px; height: 180px; display: flex; align-items: center; padding-left: 40px; gap: 18px; }
  .brand-mark { width: 44px; height: 44px; background: var(--green); }
  .brand-name { font-size: 58px; font-weight: 700; color: var(--purple); letter-spacing: 1px; }

  .address { left: 470px; top: 19px; width: 195px; height: 96px; padding: 12px 14px; color: var(--white); font-size: 17px; line-height: 1.3; }
  .address svg { vertical-align: -2px; margin-right: 4px; }

  .materials { left: 0; top: 211px; width: 662px; height: 58px; padding-left: 22px; display: flex; align-items: center;
    font-size: 24px; font-weight: 700; color: var(--text-dark); }

  .consultancy { left: 674px; top: 288px; width: 466px; height: 86px; padding: 10px 16px; font-size: 17px; line-height: 1.3; }
  .heading-purple { color: var(--purple); font-weight: 700; font-size: 17px; margin: 0 0 4px; }
  .heading-green { color: var(--green); font-weight: 700; font-size: 17px; margin: 0 0 4px; }
  .heading-white { color: var(--white); font-weight: 700; font-size: 17px; margin: 0 0 4px; }
  .body-copy { margin: 0; font-size: 17px; line-height: 1.3; }

  .commercial { left: 670px; top: 504px; width: 130px; height: 290px; padding: 10px 10px; }
  .tailored { left: 10px; top: 576px; width: 122px; height: 216px; padding: 12px 10px; color: var(--white); }
  .quote { left: 276px; top: 652px; width: 386px; height: 68px; padding: 10px 14px; }

  .contact { left: 936px; top: 660px; width: 252px; height: 156px; padding: 16px 18px; color: var(--white); font-size: 17px; }
  .contact-list { list-style: none; margin: 0; padding: 0; }
  .contact-list li { display: flex; align-items: center; gap: 8px; line-height: 1.7; }
</style>
</head>
<body>
<div class="leaflet">
  <!-- decorative grid tiles -->
  <div class="block tile-white" style="left:0;top:0;width:465px;height:205px"></div>
  <div class="block tile-white" style="left:470px;top:120px;width:195px;height:86px"></div>
  <div class="block tile-purple" style="left:548px;top:145px;width:52px;height:58px"></div>
  <div class="block tile-white" style="left:665px;top:288px;width:535px;height:90px"></div>
  <div class="block tile-purple" style="left:1142px;top:288px;width:58px;height:86px"></div>
  <div class="block tile-white" style="left:0;top:652px;width:270px;height:193px"></div>
  <div class="block tile-white" style="left:400px;top:726px;width:262px;height:119px"></div>
  <div class="block tile-green" style="left:272px;top:744px;width:124px;height:90px"></div>
  <div class="block tile-purple" style="left:672px;top:800px;width:58px;height:45px"></div>
  <div class="block tile-white" style="left:806px;top:656px;width:124px;height:189px"></div>
  <div class="block tile-green" style="left:806px;top:745px;width:124px;height:80px"></div>
  <div class="block tile-white" style="left:674px;top:384px;width:120px;height:114px"></div>

  <div class="block photo photo-kitchen-bright" role="img" aria-label="Photo of a bright modern kitchen with white stone worktops"></div>
  <div class="block photo photo-kitchen-main" role="img" aria-label="Photo of a stone kitchen worktop with sink and gas hob"></div>
  <div class="block photo photo-island" role="img" aria-label="Photo of a long stone kitchen island in an open-plan room"></div>

  <div class="block tile-purple" style="left:1055px;top:0;width:70px;height:48px"></div>
  <div class="block tile-green" style="left:995px;top:288px;width:72px;height:48px"></div>
  <div class="block tile-green" style="left:30px;top:95px;width:82px;height:70px;display:none"></div>

  <header class="block brand tile-white">
    <span class="brand-mark"></span>
    <span class="brand-name">Trelvax</span>
  </header>

  <address class="block address tile-green" style="font-style:normal">
    <svg width="14" height="18" viewBox="0 0 14 18"><path d="M7 0a7 7 0 0 0-7 7c0 5 7 11 7 11s7-6 7-11a7 7 0 0 0-7-7zm0 10a3 3 0 1 1 0-6 3 3 0 0 1 0 6z" fill="#fff"/></svg>28-34 Harrow Lane<br>London, EC2N 7QD
  </address>

  <div class="block materials tile-green">Granite • Marble • Quartz • Solid surfaces • Ceramic</div>

  <section class="block consultancy tile-white">
    <h2 class="heading-purple">Consultancy Service</h2>
    <p class="body-copy">We offer a full support and consultancy service to a range of trade professionals.</p>
  </section>

  <section class="block commercial tile-white">
    <h2 class="heading-green">Commercial Projects</h2>
    <p class="body-copy">We are a trusted provider of specialist retail, office and commercial contract stone supply, fit and repair services.</p>
  </section>

  <section class="block tailored tile-purple">
    <h2 class="heading-white">Specifically Tailored</h2>
    <p class="body-copy">Our services can be used in any space where stone surfaces are required.</p>
  </section>

  <section class="block quote tile-white">
    <h2 class="heading-purple">Request a Quote</h2>
    <p class="body-copy">We welcome enquiries – please contact us and we will be happy to assist.</p>
  </section>

  <section class="block contact tile-green">
    <ul class="contact-list">
      <li><svg width="14" height="14" viewBox="0 0 24 24"><path d="M6.6 10.8a15 15 0 0 0 6.6 6.6l2.2-2.2c.3-.3.7-.4 1-.2 1.1.4 2.3.6 3.6.6.6 0 1 .4 1 1V20c0 .6-.4 1-1 1A17 17 0 0 1 3 4c0-.6.4-1 1-1h3.5c.6 0 1 .4 1 1 0 1.3.2 2.5.6 3.6.1.3 0 .7-.2 1z" fill="#fff"/></svg>02075550148</li>
      <li><svg width="14" height="14" viewBox="0 0 24 24"><rect x="6" y="1" width="12" height="22" rx="2" fill="#fff"/><rect x="8" y="4" width="8" height="14" fill="#8dc63f"/></svg>07700900362</li>
      <li><svg width="14" height="14" viewBox="0 0 24 24"><rect x="2" y="5" width="20" height="14" fill="#fff"/><path d="M2 5l10 8 10-8" stroke="#8dc63f" stroke-width="2" fill="none"/></svg>hello@trelvax.co.uk</li>
      <li><svg width="14" height="14" viewBox="0 0 24 24"><circle cx="12" cy="12" r="10" fill="none" stroke="#fff" stroke-width="2"/><path d="M2 12h20M12 2c3 3 3 17 0 20M12 2c-3 3-3 17 0 20" stroke="#fff" stroke-width="2" fill="none"/></svg>www.trelvax.co.uk</li>
    </ul>
  </section>
</div>
</body>
</html>
```